Container for chopstick set. Box or cylinder

The package will hold 5 pairs of black chopsticks (see uploaded file). These are the things that we liked from the attached files:
Idea 1: Kraft paper, illustration, the contrast of the green color with black illustration + text and green background
Idea 2: cylinder
Idea 3: Illustration of product, slide opening box type

Target Market(s)

The target market are women with families around between the ages of 25-50.

Font styles to use
Other font styles liked:
• Please see logo

Colors

Designer to choose colors to be used in the design.

Requirements
Must have
• Please incorporate our logo into the package (it's ok to change the colors of our logo), but our logo shouldn't cover a significant surface of the package
• Be creative with color(s).
Nice to have
• Possible designs:
• 1) Cylinder (4cm diameter, 25cm height)
• Alternative A: black matte background
• Alternative B: similar colors in Idea 1 with Kraft paper background.
• 2) Slide opening box (7cm x 25cm x 1cm)
• Alternative C: white box which incorporates our green logo (bottom right)

```html
<!DOCTYPE html>
<html lang="en">
<head>
<meta charset="utf-8">
<title>Sagewood Chopstick Tube Label</title>
<link href="https://fonts.googleapis.com/css2?family=Anton&display=swap" rel="stylesheet">
<style>
  :root {
    --backdrop: #f4f5f7;
    --kraft: #c49a6c;
    --kraft-deep: #b88d5f;
    --ink: #141210;
    --leaf: #a6d46a;
    --paper-white: #ffffff;
  }
  * { margin: 0; padding: 0; box-sizing: border-box; }
  html, body {
    width: 964px;
    height: 1200px;
    overflow: hidden;
    background: var(--backdrop);
  }
  .canvas {
    position: relative;
    width: 964px;
    height: 1200px;
  }
  .tube-label {
    position: absolute;
    left: 348px;
    top: 152px;
    width: 272px;
    height: 920px;
    background: linear-gradient(90deg, var(--kraft-deep) 0%, var(--kraft) 18%, var(--kraft) 82%, var(--kraft-deep) 100%);
  }
  .brand {
    position: absolute;
    left: 0;
    top: 52px;
    width: 100%;
    display: flex;
    flex-direction: column;
    align-items: center;
    gap: 14px;
  }
  .brand-dot {
    width: 62px;
    height: 62px;
    border-radius: 50%;
    background: var(--leaf);
  }
  .brand-name {
    font-family: "Anton", sans-serif;
    font-size: 30px;
    letter-spacing: 1px;
    color: var(--paper-white);
    line-height: 1;
  }
  .claim {
    position: absolute;
    left: 43px;
    top: 896px;
    transform-origin: 0 0;
    transform: rotate(-90deg);
    font-family: "Anton", sans-serif;
    font-size: 54px;
    line-height: 90px;
    letter-spacing: 2px;
    color: var(--ink);
    white-space: nowrap;
    text-transform: uppercase;
  }
  .claim-line { display: block; }
</style>
</head>
<body>
  <main class="canvas">
    <section class="tube-label">
      <div class="brand">
        <span class="brand-dot"></span>
        <span class="brand-name">sagewood</span>
      </div>
      <h1 class="claim">
        <span class="claim-line">5 Pairs of</span>
        <span class="claim-line">Black Chopsticks</span>
      </h1>
    </section>
  </main>
</body>
</html>
```